draft # 94 and #95- Could we see the accent pink line in more of a brush stroke and could you make the logo a little bigger and the name and title smaller. Please add the website on the front of the card and add "Locally owned and operated" in the back.
draft #58
We would like to include our tag line of the front of the card "Making memories, one dip at a time!" Could we see this tagline in the same script font used in the logo. Could you also add
"Serving Bakersfield & Surrounding Areas" on the back of the card, above the watermark
Mossworks-Could we see the coordinating stationery and envelopes for draft #58
Thank you all for your submissions! We are off to a good start. Please show us more options using the chocolate brown as the primary color and using pink as the accent color. Also please remember to include "Locally owned and operated." on the back of the card. (without quotation marks, of course)
We would also like to see the fountain part of the logo or the initials as a watermark on the back of the card.
We want to make sure the font on the logo is bigger than the other font size used on the rest of the card.
Draft # 54 could we see the front logo a little bigger and add Locally owned and operated on the back.
Thanks!=)

```html
<!DOCTYPE html>
<html lang="en">
<head>
<meta charset="utf-8">
<title>Rosa-Bellamy's business cards</title>
<link href="https://fonts.googleapis.com/css2?family=Cinzel:wght@400;600&family=Great+Vibes&family=Open+Sans:wght@400;600&display=swap" rel="stylesheet">
<style>
  :root{
    --chocolate:#3a1015;
    --pink:#e2306b;
    --pink-soft:#f07aa0;
    --pink-line:#d8266a;
    --frame-dark:#7a1a35;
    --paper:#ffffff;
    --card-edge:#eadde0;
  }
  *{margin:0;padding:0;box-sizing:border-box}
  html,body{width:1200px;height:664px;overflow:hidden;background:var(--paper)}
  body{position:relative;font-family:'Open Sans',sans-serif}

  .card{position:absolute;top:96px;width:268px;height:492px;border-radius:20px;overflow:hidden}
  .card--dark{background:var(--chocolate)}
  .card--light{background:var(--paper);box-shadow:0 0 0 1px var(--card-edge)}
  .card__frame{position:absolute;inset:10px;border-radius:14px;border:3px solid var(--pink-line);opacity:.85}
  .card--dark .card__frame{border-color:var(--frame-dark)}
  .front-1{left:19px}
  .back-1{left:307px}
  .front-2{left:605px}
  .back-2{left:893px}

  .brand{
    position:absolute;top:58px;left:0;right:0;text-align:center;
    font-family:'Cinzel',serif;font-weight:600;font-size:23px;letter-spacing:.5px;
  }
  .card--dark .brand{color:var(--pink)}
  .card--light .brand{color:var(--chocolate)}
  .brand__dot{display:block;margin:0 auto 12px;width:40px;height:40px;border-radius:50%}
  .card--dark .brand__dot{background:var(--pink)}
  .card--light .brand__dot{background:var(--pink-line)}

  .tagline{
    position:absolute;top:172px;left:16px;right:16px;text-align:center;
    font-family:'Great Vibes',cursive;font-size:19px;line-height:1.2;
  }
  .card--dark .tagline{color:var(--pink-soft)}
  .card--light .tagline{color:var(--pink-line)}

  .person{position:absolute;top:262px;left:0;right:0;text-align:center;font-family:'Cinzel',serif}
  .person__name{font-size:17px;letter-spacing:1.5px}
  .person__title{font-size:11px;letter-spacing:2px;margin-top:6px}
  .card--dark .person{color:var(--pink-soft)}
  .card--light .person{color:var(--chocolate)}

  .contact{
    position:absolute;top:372px;left:50%;transform:translateX(-50%);width:150px;height:96px;
    padding:10px 12px;border-radius:8px;font-size:8.5px;line-height:1.5;color:#fff;
  }
  .card--dark .contact{background:rgba(226,48,107,.35)}
  .card--light .contact{background:var(--chocolate)}
  .contact p{white-space:nowrap}
  .contact__gap{margin-top:7px}
  .contact__web{font-weight:600}

  .watermark{
    position:absolute;top:130px;left:0;right:0;text-align:center;
    font-family:'Cinzel',serif;font-weight:600;font-size:22px;
  }
  .watermark__dot{display:block;margin:0 auto 14px;width:80px;height:80px;border-radius:50%}
  .back-1 .watermark{color:rgba(226,48,107,.2)}
  .back-1 .watermark__dot{background:rgba(226,48,107,.14)}
  .back-2 .watermark{color:var(--chocolate)}
  .back-2 .watermark__dot{background:var(--chocolate)}

  .locally{
    position:absolute;top:300px;left:0;right:0;text-align:center;
    font-family:'Cinzel',serif;font-size:11px;letter-spacing:1.5px;
  }
  .back-1 .locally{color:var(--pink-soft)}
  .back-2 .locally{color:var(--pink-line)}
</style>
</head>
<body>
  <section class="card card--dark front-1">
    <div class="card__frame"></div>
    <div class="brand"><span class="brand__dot"></span>Rosa-Bellamy's</div>
    <p class="tagline">Making memories, one dip at a time!</p>
    <div class="person"><p class="person__name">Marisol Varela</p><p class="person__title">OWNER</p></div>
    <div class="contact">
      <p>Phone: 661-555-0142</p>
      <p>Fax: 661-555-0187</p>
      <p class="contact__gap">marisol@rosabellamys.com</p>
      <p class="contact__web">www.rosabellamys.com</p>
    </div>
  </section>

  <section class="card card--dark back-1">
    <div class="card__frame"></div>
    <div class="watermark"><span class="watermark__dot"></span>Rosa-Bellamy's</div>
    <p class="locally">Locally owned and operated.</p>
  </section>

  <section class="card card--light front-2">
    <div class="card__frame"></div>
    <div class="brand"><span class="brand__dot"></span>Rosa-Bellamy's</div>
    <p class="tagline">Making memories, one dip at a time!</p>
    <div class="person"><p class="person__name">Marisol Varela</p><p class="person__title">OWNER</p></div>
    <div class="contact">
      <p>Phone: 661-555-0142</p>
      <p>Fax: 661-555-0187</p>
      <p class="contact__gap">marisol@rosabellamys.com</p>
      <p class="contact__web">www.rosabellamys.com</p>
    </div>
  </section>

  <section class="card card--light back-2">
    <div class="card__frame"></div>
    <div class="watermark"><span class="watermark__dot"></span>Rosa-Bellamy's</div>
    <p class="locally">Locally owned and operated.</p>
  </section>
</body>
</html>
```